Visitenkarten-Design Neutrale Verzollungs Agentur für den Grenzverkehr des Zollwesens
Sehr schnelle Umsetzung nach unserer Vorstellung,und sehr netter und guter Umgang in der Kominikation. tolvix hat unsere erwartung zu 100 % übertroffen.
Zielgruppe
Wir sind eine Neutrale Verzollungs Agentur für den Grenzverkehr des Zollwesens
Bluefield & Meridian Group
Wir führen für Kunden die Zollabwicklungen ab.
Seefracht - Bahnfracht-Luftfracht-LKW Fracht
Cargo - Hersteller Firmen und Endknden International
Aufgabenstellung
Rückseite sollte mitgestaltet werden

```html
<!DOCTYPE html>
<html lang="de">
<head>
<meta charset="utf-8">
<title>Grenzwerk – Visitenkarte</title>
<link href="https://fonts.googleapis.com/css2?family=Nunito:wght@700&family=Open+Sans:wght@600&family=Questrial&display=swap" rel="stylesheet">
<style>
  :root {
    --backdrop: #c8c8c8;
    --paper: #ffffff;
    --ink: #4a4a4a;
    --ink-strong: #3f3f3f;
    --brand-blue: #4a8fd0;
    --stripe: #ecebf4;
    --divider: #a9c3da;
    --back-light: #3a86a8;
    --back-mid: #2a6a98;
    --back-dark: #0b3a72;
    --globe-glow: #6aa6a0;
    --logo-light: #c7dcf2;
  }
  html, body {
    margin: 0;
    width: 1073px;
    height: 1200px;
    overflow: hidden;
    background: var(--backdrop);
  }
  .card {
    position: absolute;
    left: 140px;
    width: 791px;
    height: 455px;
    overflow: hidden;
  }
  .card--front { top: 141px; background: var(--paper); }
  .card--back {
    top: 658px;
    left: 144px;
    width: 787px;
    background: linear-gradient(90deg, var(--back-light) 0%, var(--back-mid) 50%, var(--back-dark) 100%);
  }
  .stripes {
    position: absolute;
    left: 0; top: 36px;
    width: 791px; height: 104px;
    background: repeating-linear-gradient(180deg, var(--stripe) 0 2px, transparent 2px 10px);
  }
  .brand-plate {
    position: absolute;
    left: 88px; top: 68px;
    width: 238px; height: 80px;
    background: var(--paper);
  }
  .brand-name {
    position: absolute;
    left: 103px; top: 96px;
    margin: 0;
    font: 700 37px/1 "Nunito", sans-serif;
    color: var(--ink-strong);
  }
  .regions {
    position: absolute;
    left: 390px; top: 128px;
    margin: 0;
    font: 600 15px/1 "Open Sans", sans-serif;
    color: var(--ink-strong);
  }
  .company {
    position: absolute;
    right: 468px; top: 256px;
    margin: 0;
    text-align: right;
    font: 700 20px/24px "Nunito", sans-serif;
    color: var(--brand-blue);
  }
  .address, .contact {
    position: absolute;
    margin: 0;
    font: 400 20px/25px "Questrial", sans-serif;
    color: var(--ink);
    font-style: normal;
  }
  .address { right: 468px; top: 336px; text-align: right; }
  .divider {
    position: absolute;
    left: 381px; top: 251px;
    width: 1px; height: 164px;
    background: var(--divider);
  }
  .contact { left: 449px; }
  .contact--phone { top: 267px; }
  .contact--web { top: 340px; }
  .globe {
    position: absolute;
    left: 36px; top: -28px;
    width: 524px; height: 524px;
    border-radius: 50%;
    background: radial-gradient(circle at 45% 55%, var(--globe-glow) 0%, rgba(58,134,168,0.6) 45%, rgba(42,106,152,0) 72%);
    border: 1px solid rgba(255,255,255,0.45);
  }
  .brand-name--back {
    position: absolute;
    left: 446px; top: 190px;
    margin: 0;
    font: 700 47px/1 "Nunito", sans-serif;
    color: var(--logo-light);
  }
</style>
</head>
<body>
  <section class="card card--front">
    <div class="stripes"></div>
    <div class="brand-plate"></div>
    <p class="brand-name">Grenzwerk</p>
    <p class="regions">Switzerland · Germany · Denmark · France</p>

    <p class="company">Bluefield &amp; Meridian<br>Group GmbH</p>
    <address class="address">Feldgasse 18<br>A-3900 Birkenau</address>

    <div class="divider"></div>

    <p class="contact contact--phone">Tel: 02345/618 42-21<br>Fax: 02345/618 42-31</p>
    <p class="contact contact--web">E-mail: service@grenzwerk-beispiel.com<br>Web: www.grenzwerk-beispiel.com</p>
  </section>

  <section class="card card--back">
    <div class="globe" role="img" aria-label="Globe with a map of North and South America and a grid of latitude and longitude lines"></div>
    <p class="brand-name--back">Grenzwerk</p>
  </section>
</body>
</html>
```